Website Redesign using existing images, copy etc.

I'm looking for a website redesign/refresh of my current WordPress website. I would like to utilize the same photography, a new photo viewer, and an overall refresh of the entire design. This will need to be WordPress with simple accessibility to make changes as we add additional properties and make updates. We auction luxury real estate and luxury yachts for non-distressed sellers. It needs to be simple, luxurious and with ease of use for both web and especially mobile. www.MarlowenGroup.com

```html
<!DOCTYPE html>
<html lang="en">
<head>
<meta charset="utf-8">
<title>Marlowen Group – Real Estate &amp; Yachts</title>
<link rel="stylesheet" href="https://fonts.googleapis.com/css2?family=Arimo:wght@400;700&display=swap">
<style>
  :root {
    --brown: #825646;
    --brown-dark: #6e4637;
    --beige: #ece9e2;
    --nav-bg: #111318;
    --footer-bg: #000000;
    --ink: #111111;
    --white: #ffffff;
    --card-ink: #7a7a7a;
  }
  * { margin: 0; padding: 0; box-sizing: border-box; }
  html, body { width: 1200px; height: 2933px; overflow: hidden; }
  body { position: relative; background: var(--white); font-family: "Arimo", Arial, sans-serif; color: var(--ink); }
  .abs { position: absolute; }
  .center-text { text-align: center; }

  /* Top navigation */
  .topbar { left: 0; top: 0; width: 1200px; height: 74px; background: var(--nav-bg); }
  .topbar-mark { left: 111px; top: 8px; width: 58px; height: 58px; border: 2px solid var(--white); border-radius: 50%; }
  .topbar-link { top: 25px; color: var(--white); font-weight: 700; font-size: 18px; transform: translateX(-50%); white-space: nowrap; }
  .topbar-link.is-active::before { content: ""; position: absolute; left: -10px; right: -10px; top: -10px; height: 2px; background: #8a8c92; }

  /* Hero */
  .hero { left: 0; top: 74px; width: 1200px; height: 526px;
    background: linear-gradient(180deg, #3a3b40 0%, #4a4540 45%, #3b352e 80%, #2c2f22 100%); }
  .hero-brand { left: 0; top: 188px; width: 1200px; display: flex; justify-content: center; align-items: center; gap: 22px; color: var(--white); }
  .hero-brand-mark { width: 60px; height: 60px; border: 3px solid var(--white); border-radius: 50%; }
  .hero-brand-name { font-size: 40px; letter-spacing: 14px; font-weight: 400; }
  .hero-tagline { left: 0; top: 280px; width: 1200px; color: var(--white); font-size: 30px; }

  .framed-btn { border: 1px solid; padding: 6px; }
  .framed-btn span { display: flex; height: 100%; align-items: center; justify-content: center; font-size: 14px; letter-spacing: .2px; text-transform: uppercase; white-space: nowrap; }
  .framed-btn.on-dark { border-color: #d9d9d9; }
  .framed-btn.on-dark span { background: rgba(90, 90, 92, .85); color: var(--white); }
  .framed-btn.on-light { border-color: var(--brown); }
  .framed-btn.on-light span { background: var(--brown); color: var(--white); }

  /* Intro */
  .intro-photo { left: 147px; top: 687px; width: 347px; height: 288px;
    background: linear-gradient(180deg, #4f7a3a 0%, #b7ad97 45%, #c98e82 75%, #5f9a3a 100%); }
  .intro-col { left: 572px; width: 480px; }
  .intro-title { top: 687px; font-size: 19px; font-weight: 700; }
  .intro-sub { top: 720px; font-size: 16px; color: var(--brown); }
  .intro-copy { top: 756px; font-size: 16.5px; line-height: 30px; }
  .rule { height: 2px; background: var(--brown); top: 947px; }
  .rule-mark { left: 793px; top: 929px; width: 38px; height: 38px; border: 2px solid var(--ink); border-radius: 50%; }

  /* Featured */
  .featured-band { left: 0; top: 1060px; width: 1200px; height: 248px; background: var(--brown); }
  .featured-base { left: 0; top: 1308px; width: 1200px; height: 335px; background: var(--beige); }
  .section-title { left: 0; width: 1200px; font-size: 37px; }
  .section-underline { height: 2px; }
  .press-card { top: 1247px; width: 225px; height: 117px; background: var(--white); box-shadow: 0 2px 6px rgba(0,0,0,.12);
    display: flex; align-items: center; justify-content: center; color: var(--card-ink); font-size: 19px; font-weight: 700; }
  .featured-copy { left: 0; top: 1400px; width: 1200px; font-size: 16.5px; line-height: 30px; }

  /* Sold gallery */
  .gallery-photo { }
  .gallery-arrow { top: 2142px; }
  .sold-copy { left: 0; top: 2207px; width: 1200px; font-size: 16.5px; line-height: 30px; }

  /* Footer */
  .footer { left: 0; top: 2566px; width: 1200px; height: 367px; background: var(--footer-bg); }
  .footer-link { top: 2633px; color: var(--white); font-weight: 700; font-size: 19px; transform: translateX(-50%); }
  .footer-mark { left: 564px; top: 2595px; width: 74px; height: 74px; border: 2px solid var(--white); border-radius: 50%; }
  .social-tile { top: 2697px; width: 22px; height: 22px; background: var(--white); border-radius: 2px; }
  .signup-title { left: 0; top: 2760px; width: 1180px; color: var(--white); font-size: 19px; font-weight: 700; }
  .signup-input { left: 488px; top: 2795px; width: 146px; height: 30px; background: #3c3c3c; color: #c9c9c9; font-size: 15px; padding: 6px 17px; }
  .signup-submit { left: 640px; top: 2795px; width: 73px; height: 30px; border: 1px solid var(--brown); padding: 3px; }
  .signup-submit span { display: flex; height: 100%; align-items: center; justify-content: center; background: var(--brown); color: var(--white); font-size: 14px; }
  .copyright { left: 0; top: 2887px; width: 1200px; color: var(--white); font-size: 16px; }
</style>
</head>
<body>

  <!-- Top navigation -->
  <header class="abs topbar">
    <div class="abs topbar-mark"></div>
    <a class="abs topbar-link is-active" style="left:516px">Buy</a>
    <a class="abs topbar-link" style="left:611px">Sales</a>
    <a class="abs topbar-link" style="left:716px">About</a>
    <a class="abs topbar-link" style="left:833px">Contact</a>
    <a class="abs topbar-link" style="left:989px">800-555-0148</a>
  </header>

  <!-- Hero -->
  <section class="abs hero" role="img" aria-label="Dusk photograph of a large craftsman-style house with stone pillars and a two-car garage"></section>
  <div class="abs hero-brand">
    <div class="hero-brand-mark"></div>
    <div class="hero-brand-name">MARLOWEN GROUP</div>
  </div>
  <p class="abs hero-tagline center-text">Real Estate &amp; Yachts</p>
  <a class="abs framed-btn on-dark" style="left:320px;top:373px;width:241px;height:52px"><span>Browser Upcoming Auctions</span></a>
  <a class="abs framed-btn on-dark" style="left:636px;top:373px;width:242px;height:52px"><span>Browser Past Successes</span></a>

  <!-- Intro -->
  <div class="abs intro-photo" role="img" aria-label="Photograph of a two-storey home with a wraparound porch and flower beds under tall trees"></div>
  <h2 class="abs intro-col intro-title center-text">Over One Billion Dollars of Auctions Marketed</h2>
  <p class="abs intro-col intro-sub center-text">Real Estate &amp; Yachts</p>
  <p class="abs intro-col intro-copy center-text">The experience of hearing the auctioneer’s final proclamation of<br>“SOLD!” is unparalleled. Whether it’s the initial meeting with the<br>seller at their estate or yacht, or the triumphant raising of the<br>paddle by the winning buyer, we relish every moment of the pro-<br>cess and the ensuing festivities. We’re confident that you will, too.</p>
  <div class="abs rule" style="left:581px;width:194px"></div>
  <div class="abs rule-mark"></div>
  <div class="abs rule" style="left:848px;width:195px"></div>

  <!-- As featured in -->
  <section class="abs featured-band"></section>
  <section class="abs featured-base"></section>
  <h2 class="abs section-title center-text" style="top:1143px;color:var(--white)">As Featured In</h2>
  <div class="abs section-underline" style="left:538px;top:1190px;width:123px;background:#e6d6cf"></div>
  <div class="abs press-card" style="left:112px">Harbor Ledger</div>
  <div class="abs press-card" style="left:362px">Estate Quarterly</div>
  <div class="abs press-card" style="left:614px">Capital Weekly</div>
  <div class="abs press-card" style="left:865px">The Market Review</div>
  <p class="abs featured-copy center-text">By offering top-tier properties and vessels globally, along with strategic auction dates, exceptional<br>marketing tactics, and a diligent public relations team, even the most prominent media outlets have<br>taken notice. Check out some of our latest press features.</p>
  <a class="abs framed-btn on-light" style="left:548px;top:1513px;width:104px;height:51px"><span style="text-transform:none;font-size:13px">View More</span></a>

  <!-- Sold by auctions -->
  <h2 class="abs section-title center-text" style="top:1718px;left:4px">Sold by Auctions</h2>
  <div class="abs section-underline" style="left:543px;top:1764px;width:123px;background:var(--ink)"></div>
  <div class="abs gallery-photo" style="left:175px;top:1820px;width:379px;height:308px;background:linear-gradient(180deg,#8fa0b0 0%,#d8d2c6 45%,#5d7a4d 100%)" role="img" aria-label="Photograph of a white modern estate with a stone walkway at dusk"></div>
  <div class="abs gallery-photo" style="left:581px;top:1820px;width:208px;height:141px;background:linear-gradient(180deg,#e6ecf2 0%,#b5a79a 60%,#5a7a3c 100%)" role="img" aria-label="Photograph of a brick and siding two-storey house"></div>
  <div class="abs gallery-photo" style="left:815px;top:1820px;width:210px;height:141px;background:linear-gradient(180deg,#2f74c9 0%,#c7a58e 60%,#4f8a3a 100%)" role="img" aria-label="Photograph of a stucco house with a red roof under blue sky"></div>
  <div class="abs gallery-photo" style="left:581px;top:1988px;width:208px;height:140px;background:linear-gradient(180deg,#5c6a80 0%,#c9c3bc 55%,#3a4a2e 100%)" role="img" aria-label="Photograph of a white farmhouse with lit windows at dusk"></div>
  <div class="abs gallery-photo" style="left:815px;top:1988px;width:210px;height:140px;background:linear-gradient(180deg,#2f6fc4 0%,#b89b8a 55%,#4c8a36 100%)" role="img" aria-label="Photograph of a brick and stone house with a green lawn"></div>
  <svg class="abs gallery-arrow" style="left:505px" width="16" height="22" viewBox="0 0 16 22"><polygon points="14,1 2,11 14,21" fill="var(--brown)"/></svg>
  <svg class="abs gallery-arrow" style="left:540px" width="16" height="22" viewBox="0 0 16 22"><polygon points="2,1 14,11 2,21" fill="var(--brown)"/></svg>
  <p class="abs sold-copy center-text">Marlowen Group is a top-tier destination for luxury property auctions, having overseen the auction market-<br>ing of numerous high-end estates and yachts. Our team of luxury home auction experts is committed<br>to helping property owners obtain the best value for their assets while ensuring a timely sale. Whether<br>you have an expansive compound or a metropolitan penthouse, Marlowen Group has the necessary<br>skills and expertise to facilitate various luxury real estate auctions.</p>
  <a class="abs framed-btn on-light" style="left:320px;top:2426px;width:241px;height:51px"><span>Learn More - About Us</span></a>
  <a class="abs framed-btn on-light" style="left:636px;top:2426px;width:242px;height:51px"><span>Browser Coming Auctions</span></a>

  <!-- Footer -->
  <footer class="abs footer"></footer>
  <a class="abs footer-link" style="left:288px">Home</a>
  <a class="abs footer-link" style="left:401px">Buy</a>
  <a class="abs footer-link" style="left:503px">Sell</a>
  <div class="abs footer-mark"></div>
  <a class="abs footer-link" style="left:710px">About</a>
  <a class="abs footer-link" style="left:827px">Blog</a>
  <a class="abs footer-link" style="left:951px">Contact</a>
  <div class="abs social-tile" style="left:545px"></div>
  <div class="abs social-tile" style="left:573px"></div>
  <div class="abs social-tile" style="left:602px"></div>
  <div class="abs social-tile" style="left:631px"></div>
  <p class="abs signup-title center-text">Sign Up for Marlowen Alerts</p>
  <div class="abs signup-input">Email</div>
  <a class="abs signup-submit"><span>SUBMIT</span></a>
  <p class="abs copyright center-text">Copyrights 2023 Marlowen Group. All Rights Reserved.</p>

</body>
</html>
```